Legal Services Power Point

Need a PP template for a legal consulting company - we prefer the use of our logo colors. Also- emphasis on international/global business with images of the USA because we serve immigration and international business coming to the US and we will use the PP to make presentations in other countries. The Company is Merivale Law Firm PC ( logo uploaded) but we have do business outside the US as Merivale Consulting Group ( logo upoaded too)

Target Market(s)

Business clients

Industry/Entity Type

Legal/ International Cross-Border/ Immigration

Font styles to use
Sans Serif

Colors
0054AA
0677BA
7BADD7
CADEEF
E8F1F8

Requirements
Must have
• International elements, global, US, we do immigration and legal consulting for foreign business
Nice to have
• Make it look elegant as we are in the legal and consulting business.

```html
<!DOCTYPE html>
<html lang="en">
<head>
<meta charset="utf-8">
<title>Merivale Consulting Group – Presentation Template</title>
<link href="https://fonts.googleapis.com/css2?family=Nunito+Sans:wght@700;800;900&family=Open+Sans:wght@400;600;700&display=swap" rel="stylesheet">
<style>
  :root{
    --blue-deep:#0054AA;
    --blue-mid:#0677BA;
    --blue-navy:#0a3f86;
    --blue-soft:#7BADD7;
    --blue-pale:#CADEEF;
    --paper:#E8F1F8;
    --red:#d21f2b;
    --red-dark:#a8141f;
    --ink:#2b2f36;
    --stage:#cfd1d4;
  }
  *{box-sizing:border-box;margin:0;padding:0}
  html,body{width:1200px;height:675px;overflow:hidden}
  body{background:linear-gradient(135deg,#dcdedf,#c4c6c9);font-family:"Open Sans",sans-serif;color:var(--ink);position:relative}
  .slide{position:absolute;width:345px;height:194px;border-radius:12px;overflow:hidden;background:var(--paper);box-shadow:0 3px 8px rgba(0,0,0,.18)}
  .slide > *{position:absolute}
  .heading{font-family:"Nunito Sans",sans-serif;font-weight:900;font-size:11.5px;color:var(--blue-deep);letter-spacing:.2px;white-space:nowrap}
  .copy{font-size:3.5px;line-height:5.4px;color:var(--ink)}
  .copy p + p{margin-top:4px}
  .photo{display:block}
  .page-num{right:6px;bottom:5px;width:14px;height:9px;border-right:1.4px solid var(--red);border-bottom:1.4px solid var(--red);font-size:3.6px;font-weight:700;text-align:center;line-height:7px;color:var(--ink)}
  .mark-box{background:var(--paper);border:1.5px solid var(--blue-deep);display:flex;align-items:center;justify-content:center}
  .mark-box span{width:55%;height:55%;background:var(--blue-deep)}
  /* cover */
  .cover-left{left:0;top:0;width:173px;height:194px;background:#d6e6f5}
  .cover-card{left:67px;top:53px;width:211px;height:87px;background:#fff;box-shadow:0 1px 3px rgba(0,0,0,.12);text-align:center}
  .cover-card .org{font-size:6px;margin-top:20px;color:var(--ink)}
  .cover-card .title{font-family:"Nunito Sans",sans-serif;font-weight:800;font-size:13px;line-height:15.5px;color:var(--blue-deep);margin-top:4px}
  .cover-card .dashes{display:flex;justify-content:center;gap:3px;margin-top:10px}
  .cover-card .dashes i{width:6px;height:2px;background:var(--red)}
  .cover-card .dashes i+i{background:var(--blue-deep)}
  .foot{font-size:3.2px;color:#444;display:flex;align-items:center;gap:2px}
  .foot b{width:4px;height:4px;border-radius:50%;background:#333;display:inline-block}
  /* toc */
  .toc-list{left:19px;top:50px;width:128px;list-style:none}
  .toc-list li{display:flex;align-items:center;font-size:4.3px;height:12px;white-space:nowrap}
  .toc-list .n{width:14px;flex:none;font-weight:700}
  .toc-list .label{width:46px;flex:none}
  .toc-list .dots{flex:1;border-bottom:.5px solid #bbb;margin:0 8px 0 0}
  .toc-list .pg{width:8px;flex:none;text-align:right}
  /* welcome */
  .name-band{left:0;top:43px;width:204px;height:45px;background:linear-gradient(90deg,var(--blue-deep),var(--blue-navy));color:#fff;padding:10px 0 0 20px;font-family:"Nunito Sans",sans-serif;font-weight:800}
  .name-band .name{font-size:8px}
  .name-band .role{font-size:6px;margin-top:2px}
  .bio-box{left:4px;top:88px;width:168px;height:89px;background:#fff;padding:17px 14px 0 14px;box-shadow:0 1px 2px rgba(0,0,0,.1)}
  .handle{font-size:3.5px;display:flex;align-items:center;gap:3px;white-space:nowrap}
  .handle i{width:4px;height:4px;background:var(--blue-deep);display:inline-block}
  /* summary */
  .stat-panel{left:169px;top:0;width:162px;height:171px;background:linear-gradient(160deg,var(--blue-mid),var(--blue-deep) 55%,var(--blue-navy))}
  .stat{position:absolute;width:76px;text-align:center;color:#fff}
  .stat svg{display:block;margin:0 auto}
  .stat .value{font-family:"Nunito Sans",sans-serif;font-weight:800;font-size:12px;margin-top:3px}
  .stat .note{font-size:3.2px;line-height:4.6px;margin-top:2px;color:#dbe8f6}
  .rule-v{background:rgba(255,255,255,.35);width:.6px}
  /* mission */
  .icon-tile{width:21px;height:21px;background:linear-gradient(145deg,var(--blue-mid),var(--blue-deep));display:flex;align-items:center;justify-content:center;box-shadow:0 1px 2px rgba(0,0,0,.25)}
  .icon-tile.red{background:linear-gradient(145deg,#e23a44,var(--red-dark))}
  .item-title{font-size:4.2px;font-weight:700}
  /* timeline */
  .tl-date{font-size:3.6px;font-weight:700;color:var(--blue-deep);text-align:center;width:80px}
  .tl-note{font-size:3.4px;line-height:4.8px;text-align:center;width:80px}
  /* vision */
  .vision-band{left:0;top:66px;width:345px;height:103px;background:linear-gradient(90deg,var(--blue-deep),var(--blue-mid) 50%,var(--blue-deep))}
  .vision-col{position:absolute;top:12px;width:80px;text-align:center;color:#fff}
  .vision-col svg{display:block;margin:0 auto}
  .vision-col h3{font-size:5px;font-weight:700;margin-top:5px}
  .vision-col p{font-size:3.3px;line-height:4.6px;margin-top:7px;color:#e2edf8}
</style>
</head>
<body>

<!-- Cover -->
<section class="slide" style="left:36px;top:29px">
  <div class="cover-left"></div>
  <div style="left:221px;top:47px;width:65px;height:55px;background:var(--blue-deep)"></div>
  <div style="left:59px;top:84px;width:65px;height:64px;background:var(--red)"></div>
  <div class="cover-card">
    <p class="org">Merivale Consulting Group</p>
    <h1 class="title">Your Global Business<br>Consulting Company</h1>
    <div class="dashes"><i></i><i></i></div>
  </div>
  <div class="mark-box" style="left:317px;top:6px;width:24px;height:21px"><span></span></div>
  <div class="foot" style="left:18px;top:181px"><b></b>www.yourwebsite.com</div>
  <div class="foot" style="right:19px;top:181px"><b style="border-radius:0"></b>youremail@yourbrand.com</div>
</section>

<!-- Table of content -->
<section class="slide" style="left:428px;top:29px">
  <h2 class="heading" style="left:19px;top:12px">TABLE OF CONTENT</h2>
  <ol class="toc-list">
    <li><span class="n">1.</span><span class="label">Cover</span><span class="dots"></span><span class="pg">01</span></li>
    <li><span class="n">2.</span><span class="label">Your Content 1</span><span class="dots"></span><span class="pg">02</span></li>
    <li><span class="n">3.</span><span class="label">Your Content 2</span><span class="dots"></span><span class="pg">03</span></li>
    <li><span class="n">4.</span><span class="label">Your Content 3</span><span class="dots"></span><span class="pg">04</span></li>
    <li><span class="n">5.</span><span class="label">Your Content 4</span><span class="dots"></span><span class="pg">05</span></li>
    <li><span class="n">6.</span><span class="label">Your Content 5</span><span class="dots"></span><span class="pg">06</span></li>
    <li><span class="n">7.</span><span class="label">Your Content 6</span><span class="dots"></span><span class="pg">07</span></li>
    <li><span class="n">8.</span><span class="label">Your Content 7</span><span class="dots"></span><span class="pg">08</span></li>
    <li><span class="n">9.</span><span class="label">Your Content 8</span><span class="dots"></span><span class="pg">09</span></li>
    <li><span class="n">10</span><span class="label">Thank you page</span><span class="dots"></span><span class="pg">10</span></li>
  </ol>
  <div style="left:181px;top:119px;width:50px;height:45px;background:var(--blue-deep)"></div>
  <div class="photo" role="img" aria-label="Photo of a US flag waving against a sunset sky" style="left:193px;top:0;width:120px;height:154px;background:linear-gradient(180deg,#5d6f86 0%,#8c8a8e 45%,#d68f5a 70%,#3a3f4d 100%)"></div>
  <div style="left:313px;top:0;width:32px;height:29px;background:linear-gradient(135deg,#e23a44,var(--red-dark))"></div>
  <div class="page-num">2</div>
</section>

<!-- Welcome message -->
<section class="slide" style="left:819px;top:29px">
  <h2 class="heading" style="left:20px;top:16px">WELCOME MESSAGE</h2>
  <div style="left:210px;top:37px;width:109px;height:59px;background:var(--red)"></div>
  <div class="name-band"><p class="name">Your Name Here</p><p class="role">Public Speaker</p></div>
  <div class="bio-box copy">Lorem ipsum dolor sit amet, consectetur adipiscing elit. Integer id consectetur nisl. Nam ligula sapien, efficitur nec mauris a, interdum accumsan libero. Pellentesque placerat blandit felis, sed finibus mauris. Donec ut mauris ante. Integer interdum libero ac nisi hendrerit, non laoreet magna venenatis. Vestibulum congue lorem mi, blandit congue justo vestibulum nec. Suspendisse rutrum quam id velit aliquet ornare.</div>
  <div class="photo" role="img" aria-label="Portrait photo of the public speaker" style="left:204px;top:43px;width:109px;height:108px;background:linear-gradient(160deg,#b9bcbf,#7d8287 60%,#3a3d42)"></div>
  <div class="handle" style="left:204px;top:161px"><i></i>@your.username</div>
  <div class="handle" style="left:267px;top:161px"><i></i>@your.username</div>
  <div class="handle" style="left:204px;top:171px"><i></i>@your.username</div>
  <div class="handle" style="left:267px;top:171px"><i></i>@your.username</div>
  <div class="page-num">3</div>
</section>

<!-- Executive summary -->
<section class="slide" style="left:36px;top:244px">
  <h2 class="heading" style="left:20px;top:12px">EXECUTIVE SUMMARY</h2>
  <div class="copy" style="left:20px;top:37px;width:133px">
    <p>Lorem ipsum dolor sit amet, consectetur adipiscing elit. Sed accumsan in metus ut gravida. Vivamus blandit faucibus nulla eu volutpat. Nullam a mattis orci.</p>
    <p>Mauris nulla orci, ullamcorper a mi ut, accumsan semper ex. Vivamus tristique ipsum quis lacus faucibus rutrum.</p>
  </div>
  <div style="left:0;top:110px;width:66px;height:8px;background:var(--red)"></div>
  <div class="photo" role="img" aria-label="Photo of a hand resting on a law book" style="left:0;top:118px;width:193px;height:76px;background:linear-gradient(120deg,#e9dcd6,#8a6a55 45%,#3b2f2a)"></div>
  <div style="left:331px;top:0;width:14px;height:45px;background:var(--red)"></div>
  <div class="stat-panel">
    <div class="stat" style="left:3px;top:20px">
      <svg width="13" height="13" viewBox="0 0 24 24" fill="none" stroke="#fff" stroke-width="2"><circle cx="12" cy="12" r="9"/><circle cx="12" cy="12" r="5"/><circle cx="12" cy="12" r="1.5"/><path d="M12 12l8-8M17 4h3v3"/></svg>
      <p class="value">10.000</p><p class="note">Lorem ipsum dolor sit amet,<br>consectetur adipiscing elit.</p>
    </div>
    <div class="stat" style="left:79px;top:20px">
      <svg width="13" height="13" viewBox="0 0 24 24" fill="none" stroke="#fff" stroke-width="2"><rect x="3" y="4" width="18" height="15"/><path d="M12 4v15M6 8h3M6 11h3M15 8h3M15 11h3"/></svg>
      <p class="value">50,50%</p><p class="note">Lorem ipsum dolor sit amet,<br>consectetur adipiscing elit.</p>
    </div>
    <div class="stat" style="left:3px;top:103px">
      <svg width="13" height="13" viewBox="0 0 24 24" fill="#fff"><path d="M12 2l10 5H2z"/><rect x="4" y="9" width="2.5" height="9"/><rect x="8.5" y="9" width="2.5" height="9"/><rect x="13" y="9" width="2.5" height="9"/><rect x="17.5" y="9" width="2.5" height="9"/><rect x="2" y="19" width="20" height="3"/></svg>
      <p class="value">2.000</p><p class="note">Lorem ipsum dolor sit amet,<br>consectetur adipiscing elit.</p>
    </div>
    <div class="stat" style="left:79px;top:103px">
      <svg width="13" height="13" viewBox="0 0 24 24" fill="none" stroke="#fff" stroke-width="2"><rect x="4" y="4" width="14" height="18"/><path d="M8 2h6v4H8zM7 11h8M7 15h6M20 8l-6 9"/></svg>
      <p class="value">70,70%</p><p class="note">Lorem ipsum dolor sit amet,<br>consectetur adipiscing elit.</p>
    </div>
    <div class="rule-v" style="position:absolute;left:78px;top:16px;height:61px"></div>
    <div class="rule-v" style="position:absolute;left:78px;top:98px;height:74px"></div>
  </div>
  <div class="page-num">6</div>
</section>

<!-- About us -->
<section class="slide" style="left:428px;top:244px">
  <h2 class="heading" style="left:19px;top:12px">ABOUT US</h2>
  <div style="left:251px;top:27px;width:94px;height:8px;background:var(--blue-deep)"></div>
  <svg style="left:0;top:0" width="345" height="194" viewBox="0 0 345 194" role="img" aria-label="Photos of the Statue of Liberty and a US city skyline by the water">
    <defs>
      <linearGradient id="skyLiberty" x1="0" y1="0" x2="1" y2="1"><stop offset="0" stop-color="#6f93b8"/><stop offset=".5" stop-color="#c9cfd3"/><stop offset="1" stop-color="#6d8a7d"/></linearGradient>
      <linearGradient id="skyCity" x1="0" y1="0" x2="0" y2="1"><stop offset="0" stop-color="#b0bfd2"/><stop offset=".4" stop-color="#e3b48c"/><stop offset="1" stop-color="#3c4655"/></linearGradient>
    </defs>
    <polygon points="0,35 178,35 162,99 0,99" fill="url(#skyLiberty)"/>
    <polygon points="183,35 345,35 345,99 169,99" fill="url(#skyCity)"/>
    <polygon points="0,99 94,99 92,108 0,108" fill="#d21f2b"/>
  </svg>
  <div class="copy" style="left:19px;top:120px;width:128px">
    <p>Lorem ipsum dolor sit amet, consectetur adipiscing elit. Sed accumsan in metus ut gravida. Vivamus blandit faucibus nulla eu volutpat. Nullam a mattis orci.</p>
    <p>Mauris nulla orci, ullamcorper a mi ut, accumsan semper ex. Vivamus tristique ipsum quis lacus faucibus rutrum.</p>
  </div>
  <div style="left:172px;top:122px;width:.6px;height:58px;background:#b7c6d6"></div>
  <div class="copy" style="left:199px;top:120px;width:128px">
    <p>Lorem ipsum dolor sit amet, consectetur adipiscing elit. Sed accumsan in metus ut gravida. Vivamus blandit faucibus nulla eu volutpat. Nullam a mattis orci.</p>
    <p>Mauris nulla orci, ullamcorper a mi ut, accumsan semper ex. Vivamus tristique ipsum quis lacus faucibus rutrum.</p>
  </div>
  <div class="page-num">4</div>
</section>

<!-- Background & story -->
<section class="slide" style="left:819px;top:244px">
  <svg style="left:0;top:0" width="345" height="194" viewBox="0 0 345 194">
    <polygon points="172,0 345,0 345,118 330,112 176,14" fill="#d21f2b"/>
    <polygon points="0,81 0,194 172,194" fill="#0054AA"/>
  </svg>
  <h2 class="heading" style="left:19px;top:12px">BACKGROUND &amp; STORY</h2>
  <div class="copy" style="left:19px;top:40px;width:137px">Lorem ipsum dolor sit amet, consectetur adipiscing elit. Sed accumsan in metus ut gravida. Vivamus blandit faucibus nulla eu volutpat. Nullam a mattis orci.</div>
  <div class="photo" role="img" aria-label="Group photo of the legal consulting team in an office" style="left:175px;top:14px;width:151px;height:97px;border:1.5px solid #fff;background:linear-gradient(135deg,#3a2c26,#6b5244 50%,#2a2624)"></div>
  <div class="photo" role="img" aria-label="Photo of the Manhattan skyline at dusk" style="left:18px;top:101px;width:151px;height:78px;border:1.5px solid #fff;background:linear-gradient(180deg,#5c7ea6,#a2a9b3 50%,#c98a5b 75%,#3b3a3c)"></div>
  <div class="copy" style="left:186px;top:123px;width:140px">Lorem ipsum dolor sit amet, consectetur adipiscing elit. Sed accumsan in metus ut gravida. Vivamus blandit faucibus nulla eu volutpat. Nullam a mattis orci.</div>
  <div class="page-num">5</div>
</section>

<!-- Our mission -->
<section class="slide" style="left:36px;top:459px">
  <h2 class="heading" style="left:20px;top:12px">OUR MISSION</h2>
  <div class="photo" role="img" aria-label="Photo of a wooden judge's gavel on a desk" style="left:162px;top:0;width:183px;height:62px;background:linear-gradient(120deg,#2a1c14,#7a4e2c 55%,#c48d52 70%,#3a2416)"></div>
  <div style="left:279px;top:62px;width:66px;height:8px;background:var(--red)"></div>
  <div class="copy" style="left:20px;top:42px;width:125px">Lorem ipsum dolor sit amet, consectetur adipiscing elit. Sed accumsan in metus ut gravida. Vivamus blandit faucibus nulla eu volutpat. Nullam a mattis orci.</div>

  <div class="icon-tile" style="left:18px;top:96px"><svg width="11" height="11" viewBox="0 0 24 24" fill="none" stroke="#fff" stroke-width="2"><path d="M6 3h12l4 6-10 12L2 9zM2 9h20M9 3l3 18 3-18"/></svg></div>
  <div style="left:51px;top:94px;width:108px"><p class="item-title">Mission 1</p><p class="copy">Lorem ipsum dolor sit amet, consectetur adipiscing elit. Sed accumsan in metus ut gravida.</p></div>
  <div class="icon-tile" style="left:18px;top:146px"><svg width="11" height="11" viewBox="0 0 24 24" fill="#fff"><path d="M12 2l10 5H2z"/><rect x="4" y="9" width="2.5" height="9"/><rect x="8.5" y="9" width="2.5" height="9"/><rect x="13" y="9" width="2.5" height="9"/><rect x="17.5" y="9" width="2.5" height="9"/><rect x="2" y="19" width="20" height="3"/></svg></div>
  <div style="left:51px;top:144px;width:108px"><p class="item-title">Mission 2</p><p class="copy">Lorem ipsum dolor sit amet, consectetur adipiscing elit. Sed accumsan in metus ut gravida.</p></div>
  <div class="icon-tile red" style="left:183px;top:96px"><svg width="11" height="11" viewBox="0 0 24 24" fill="none" stroke="#fff" stroke-width="2"><path d="M12 3v18M5 21h14M4 6h16M4 6l-3 7h6zM20 6l-3 7h6z"/></svg></div>
  <div style="left:217px;top:94px;width:108px"><p class="item-title">Mission 3</p><p class="copy">Lorem ipsum dolor sit amet, consectetur adipiscing elit. Sed accumsan in metus ut gravida.</p></div>
  <div class="icon-tile" style="left:183px;top:146px"><svg width="11" height="11" viewBox="0 0 24 24" fill="#fff"><rect x="9" y="2" width="10" height="6" transform="rotate(45 14 5)"/><rect x="3" y="13" width="3" height="11" transform="rotate(45 4.5 18.5)"/><rect x="2" y="20" width="12" height="3"/></svg></div>
  <div style="left:217px;top:144px;width:108px"><p class="item-title">Mission 4</p><p class="copy">Lorem ipsum dolor sit amet, consectetur adipiscing elit. Sed accumsan in metus ut gravida.</p></div>
  <div class="page-num">9</div>
</section>

<!-- Our timeline -->
<section class="slide" style="left:428px;top:459px">
  <h2 class="heading" style="left:19px;top:12px">OUR TIMELINE</h2>
  <div style="left:316px;top:0;width:29px;height:18px;background:linear-gradient(135deg,#e23a44,var(--red-dark))"></div>
  <div style="left:0;top:176px;width:28px;height:18px;background:linear-gradient(135deg,#e23a44,var(--red-dark))"></div>
  <svg style="left:0;top:0" width="345" height="194" viewBox="0 0 345 194">
    <line x1="58" y1="111" x2="301" y2="111" stroke="#0054AA" stroke-width=".8"/>
    <g stroke="#0054AA" stroke-width=".8">
      <line x1="82" y1="111" x2="82" y2="126"/><line x1="126" y1="111" x2="126" y2="96"/><line x1="171" y1="111" x2="171" y2="126"/><line x1="215" y1="111" x2="215" y2="96"/><line x1="260" y1="111" x2="260" y2="126"/>
    </g>
    <g fill="#0054AA">
      <circle cx="82" cy="111" r="2.4"/><circle cx="126" cy="111" r="2.4"/><circle cx="171" cy="111" r="2.4"/><circle cx="215" cy="111" r="2.4"/><circle cx="260" cy="111" r="2.4"/>
      <circle cx="82" cy="126" r=".9"/><circle cx="126" cy="96" r=".9"/><circle cx="171" cy="126" r=".9"/><circle cx="215" cy="96" r=".9"/><circle cx="260" cy="126" r=".9"/>
      <circle cx="314" cy="111" r="13"/>
    </g>
    <path d="M310 104v14M310 104h9l-2 3 2 3h-9" fill="#fff" stroke="#fff" stroke-width="1.2"/>
  </svg>
  <div class="mark-box" style="left:17px;top:93px;width:41px;height:35px;box-shadow:0 1px 3px rgba(0,0,0,.2);border-width:2px"><span></span></div>
  <p class="tl-date" style="left:86px;top:55px">10 Mar 2024</p>
  <p class="tl-note" style="left:86px;top:66px">Lorem ipsum dolor sit amet, consectetur adipiscing elit. Integer id nisl.</p>
  <p class="tl-date" style="left:175px;top:55px">10 Jul 2024</p>
  <p class="tl-note" style="left:175px;top:66px">Lorem ipsum dolor sit amet, consectetur adipiscing elit. Integer id nisl.</p>
  <p class="tl-date" style="left:42px;top:137px">10 Jan 2024</p>
  <p class="tl-note" style="left:42px;top:148px">Lorem ipsum dolor sit amet, consectetur adipiscing elit. Integer id nisl.</p>
  <p class="tl-date" style="left:131px;top:137px">10 May 2024</p>
  <p class="tl-note" style="left:131px;top:148px">Lorem ipsum dolor sit amet, consectetur adipiscing elit. Integer id nisl.</p>
  <p class="tl-date" style="left:220px;top:137px">10 Sep 2024</p>
  <p class="tl-note" style="left:220px;top:148px">Lorem ipsum dolor sit amet, consectetur adipiscing elit. Integer id nisl.</p>
  <div class="page-num">7</div>
</section>

<!-- Our vision -->
<section class="slide" style="left:819px;top:459px">
  <h2 class="heading" style="left:19px;top:12px">OUR VISION</h2>
  <div style="left:327px;top:0;width:18px;height:66px;background:var(--red)"></div>
  <div style="left:0;top:169px;width:17px;height:25px;background:var(--red)"></div>
  <div class="copy" style="left:19px;top:36px;width:195px">Lorem ipsum dolor sit amet, consectetur adipiscing elit. Sed accumsan in metus ut gravida. Vivamus blandit faucibus nulla eu volutpat. Nullam a mattis orci.</div>
  <div class="vision-band">
    <div class="vision-col" style="left:16px">
      <svg width="10" height="10" viewBox="0 0 24 24" fill="none" stroke="#fff" stroke-width="2"><path d="M6 3h12l4 6-10 12L2 9zM2 9h20M9 3l3 18 3-18"/></svg>
      <h3>Vision One</h3><p>Proin imperdiet placerat velit ut placerat. Nam sollicitudin eros at nulla congue venenatis.</p>
    </div>
    <div class="rule-v" style="position:absolute;left:112px;top:14px;height:80px"></div>
    <div class="vision-col" style="left:132px">
      <svg width="10" height="10" viewBox="0 0 24 24" fill="#fff"><circle cx="12" cy="7" r="4.5"/><path d="M3 22c0-6 4-9 9-9s9 3 9 9z"/></svg>
      <h3>Vision Two</h3><p>Proin imperdiet placerat velit ut placerat. Nam sollicitudin eros at nulla congue venenatis.</p>
    </div>
    <div class="rule-v" style="position:absolute;left:231px;top:14px;height:80px"></div>
    <div class="vision-col" style="left:248px">
      <svg width="10" height="10" viewBox="0 0 24 24" fill="none" stroke="#fff" stroke-width="2"><path d="M12 3v18M5 21h14M4 6h16M4 6l-3 7h6zM20 6l-3 7h6z"/></svg>
      <h3>Vision Three</h3><p>Proin imperdiet placerat velit ut placerat. Nam sollicitudin eros at nulla congue venenatis.</p>
    </div>
  </div>
  <div class="page-num">8</div>
</section>

</body>
</html>
```